VELO Selfie Wall Design for Coworking Space

Design a striking, large-scale wall mural for VELO Hub that embodies our brand identity, incorporates Oakland-inspired elements, and enhances our coworking and event space. The design should be bold, visually engaging, and aligned with our brand aesthetic—featuring black, white, and bronze tones.
Key Requirements:
Branded Mural Design
Prominently (but tastefully) feature the VELO Hub logo.
Use abstract shapes, gradients, or geometric patterns (inspired by the VELO logo) to convey movement and connectivity.
Incorporate the tagline: “Live · Work · Play · Go” in brand-approved typography.
Avoid literal imagery—keep the design sleek and modern.
Integrated Selfie Wall
Designate a photo-friendly zone with:
Open negative space (clean background) for people to pose naturally.
A bold but simple focal point (e.g., stylized typography, an Oakland-inspired icon, or a bronze metallic accent).
Lighting-friendly elements (avoid small patterns that may clash on camera).
Oakland Nods
Subtle references to the city (e.g., abstract skyline, bridge motifs, or topographic patterns) without being literal.
Updates
After reviewing designs, management has asked that this design incorporates a "selfie" aspect where people would be encouraged to take a photo with the wall. This would leave a thoughtful area for people to pose or engage with the design on the wall. Ideally, we want people to see the wall and take a picture with the design as a background
Target Market(s)
Office Employees
Industry/Entity Type
Real Estate/Coworking
Font styles to use
Other font styles liked:
- Henderson Sans
Look and feel
Each slider illustrates characteristics of the customer's brand and the style your logo design should communicate.

```html
<!DOCTYPE html>
<html lang="en">
<head>
<meta charset="utf-8">
<title>VELO Hub — Live Work Play Go Wall</title>
<link href="https://fonts.googleapis.com/css2?family=Krona+One&display=swap" rel="stylesheet">
<style>
  :root {
    --page: #f4f4f2;
    --peach: #efba88;
    --bronze: #8f4e2e;
    --teal: #1d4252;
    --charcoal: #3a3a3a;
    --ink: #0b0b0b;
    --silver: #c4c4c4;
    --white: #ffffff;
  }
  * { margin: 0; padding: 0; box-sizing: border-box; }
  html, body {
    width: 1200px;
    height: 900px;
    overflow: hidden;
    background: var(--page);
  }
  .wall {
    position: absolute;
    top: 150px;
    left: 0;
    width: 1200px;
    height: 600px;
  }
  .wall__artwork {
    width: 1200px;
    height: 500px;
    background: linear-gradient(90deg,
      var(--peach) 0%,
      var(--teal) 22%,
      var(--bronze) 40%,
      var(--silver) 54%,
      var(--silver) 64%,
      var(--peach) 74%,
      var(--charcoal) 86%,
      var(--ink) 100%);
  }
  .brand {
    position: absolute;
    top: 40px;
    left: 622px;
    display: flex;
    align-items: center;
    gap: 14px;
  }
  .brand__mark {
    width: 30px;
    height: 30px;
    background: var(--bronze);
  }
  .brand__name {
    font-family: "Krona One", sans-serif;
    font-size: 26px;
    letter-spacing: 3px;
    color: var(--ink);
  }
  .tagline {
    position: absolute;
    left: 0;
    bottom: 0;
    width: 1200px;
    height: 100px;
    background: var(--ink);
    display: flex;
    align-items: center;
    justify-content: space-between;
    padding: 0 70px;
    font-family: "Krona One", sans-serif;
    font-size: 40px;
    letter-spacing: 10px;
    color: var(--white);
  }
  .tagline__dot { font-size: 30px; letter-spacing: 0; }
</style>
</head>
<body>
  <div class="wall">
    <div class="wall__artwork" role="img" aria-label="Bold geometric mural of angled panels in peach, bronze, teal, charcoal, silver and black"></div>
    <div class="brand">
      <span class="brand__mark"></span>
      <span class="brand__name">VELO</span>
    </div>
    <div class="tagline">
      <span>LIVE</span><span class="tagline__dot">•</span>
      <span>WORK</span><span class="tagline__dot">•</span>
      <span>PLAY</span><span class="tagline__dot">•</span>
      <span>GO</span>
    </div>
  </div>
</body>
</html>
```